Design a large parking banner – mandatory ticket validation in the shop

Banner Size:
548 cm (width) x 154 cm (height)
Note: The banner will be placed in a metal frame at our parking lot entrance, fully visible to every incoming truck driver. The message must be easy to read from a distance.
Goal of the Banner:
To inform all truck drivers that they must validate their entry ticket inside the shop, even if they are parking for a short time.
The message must be displayed in multiple languages for international drivers.
Mandatory Content:
Main message – in multiple languages (clearly separated or stacked):
Dutch (NL): Vergeet je ticket niet te valideren in de shop – verplicht, ook bij kort parkeren!
French (FR): N'oubliez pas de valider votre ticket à la boutique – obligatoire, même pour un court arrêt !
English (EN): Don't forget to validate your entry ticket in the shop – mandatory, even for short stops!
German (DE): Vergessen Sie nicht, Ihr Einfahrticket im Shop zu entwerten – Pflicht, auch bei kurzem Parken!
Polish (PL): Nie zapomnij zatwierdzić biletu w sklepie – obowiązkowe, nawet przy krótkim postoju!
Romanian (RO): Nu uitați să validați biletul în magazin – obligatoriu, chiar și pentru opriri scurte!
You can include more languages if space allows, but these are essential.
Opening Hours Block (in one section below):
Shop Opening Hours
Mon – Fri: 05:30 – 22:00
Sat & Sun: 08:00 – 22:00
Style & Branding:
The design must match the visual identity of Haulport 41Ter
Please refer to the attached photos of existing parking signage for guidance on colors, typography, and layout style
Our logo (attached) must be clearly visible and professionally integrated
Feel free to use icons or pictograms to visually support the message (e.g., ticket, truck, arrow)
Readability is key – large, bold text and high contrast colors that are visible from a distance
Target Audience:
International truck drivers – people who need fast, clear communication. Not everyone speaks the local language, so visual clarity and multilingual messaging are critical.
File Requirements:
Print-ready file (PDF or EPS) – 300 dpi at 1:10 scale
Include 5 cm bleed on all sides
Provide open source files if possible (AI or PSD)

```html
<!DOCTYPE html>
<html lang="nl">
<head>
<meta charset="utf-8">
<title>Haulport 41Ter – Parking Banner</title>
<link href="https://fonts.googleapis.com/css2?family=Poppins:wght@600;700;800&family=Bebas+Neue&display=swap" rel="stylesheet">
<style>
  :root {
    --navy: #25264f;
    --navy-deep: #1f2046;
    --blue: #1f7fd0;
    --blue-dark: #1a4f9a;
    --red: #d3151c;
    --white: #ffffff;
    --page: #eef0f4;
  }
  * { margin: 0; padding: 0; box-sizing: border-box; }
  html, body {
    width: 1200px;
    height: 894px;
    overflow: hidden;
    background: var(--page);
  }
  .canvas {
    position: relative;
    width: 1200px;
    height: 894px;
    display: flex;
    align-items: center;
  }
  .banner {
    position: relative;
    width: 1200px;
    height: 320px;
    background: var(--navy);
    overflow: hidden;
    font-family: "Poppins", sans-serif;
  }

  .brand {
    position: absolute;
    left: 34px;
    top: 26px;
    color: var(--white);
    font-weight: 800;
    font-size: 40px;
    line-height: 44px;
    letter-spacing: 0.5px;
  }

  .accent {
    position: absolute;
    opacity: 0.85;
  }
  .accent--left {
    left: 268px;
    top: 24px;
    width: 160px;
    height: 150px;
    background: linear-gradient(200deg, var(--blue) 0%, rgba(31,127,208,0) 85%);
    clip-path: polygon(90% 0, 100% 0, 10% 100%, 0 100%);
  }
  .accent--right {
    left: 920px;
    top: 128px;
    width: 150px;
    height: 132px;
    background: linear-gradient(20deg, var(--blue) 10%, rgba(31,127,208,0) 90%);
    clip-path: polygon(92% 0, 100% 0, 10% 100%, 0 100%);
  }

  .message {
    position: absolute;
    height: 31px;
    display: flex;
    align-items: center;
    padding-left: 48px;
    color: var(--white);
    font-weight: 700;
    font-size: 12.5px;
    white-space: nowrap;
    clip-path: polygon(30px 0, 100% 0, calc(100% - 30px) 100%, 0 100%);
  }
  .message--blue { background: linear-gradient(90deg, var(--blue) 0%, var(--blue-dark) 70%, var(--navy-deep) 100%); }
  .message--red  { background: var(--red); }

  .message:nth-of-type(1) { left: 417px; top: 24px;  width: 706px; }
  .message:nth-of-type(2) { left: 375px; top: 64px;  width: 732px; }
  .message:nth-of-type(3) { left: 331px; top: 105px; width: 735px; }
  .message:nth-of-type(4) { left: 287px; top: 145px; width: 733px; }
  .message:nth-of-type(5) { left: 244px; top: 185px; width: 732px; }
  .message:nth-of-type(6) { left: 200px; top: 225px; width: 732px; }

  .hours {
    position: absolute;
    left: 0;
    bottom: 0;
    width: 1200px;
    height: 40px;
    background: var(--blue-dark);
  }
  .hours__label {
    position: absolute;
    left: 0; top: 0;
    width: 412px; height: 40px;
    background: var(--white);
    clip-path: polygon(0 0, 100% 0, calc(100% - 30px) 100%, 0 100%);
    color: var(--navy);
    font-weight: 700;
    font-size: 24px;
    line-height: 40px;
    padding-left: 26px;
  }
  .hours__block {
    position: absolute;
    top: 0;
    height: 40px;
    color: var(--white);
    font-family: "Bebas Neue", "Oswald", sans-serif;
    font-size: 33px;
    line-height: 42px;
    text-align: center;
    background: linear-gradient(90deg, var(--blue) 0%, var(--blue-dark) 100%);
    clip-path: polygon(30px 0, 100% 0, calc(100% - 30px) 100%, 0 100%);
  }
  .hours__block--week { left: 382px; width: 428px; }
  .hours__block--weekend { left: 806px; width: 430px; background: linear-gradient(90deg, var(--blue-dark) 0%, var(--blue) 60%, var(--blue-dark) 100%); }
  .hours__gap {
    position: absolute;
    left: 790px; top: 0;
    width: 50px; height: 40px;
    background: var(--white);
    clip-path: polygon(32px 0, 50px 0, 18px 100%, 0 100%);
  }
</style>
</head>
<body>
<div class="canvas">
  <section class="banner" aria-label="Parkeerbanner: ticket valideren in de shop">
    <div class="brand">HAULPORT<br>41TER</div>

    <div class="accent accent--left"></div>
    <div class="accent accent--right"></div>

    <div class="messages">
      <p class="message message--blue" lang="nl">Vergeet je ticket niet te valideren in de shop – verplicht, ook bij kort parkeren!</p>
      <p class="message message--red" lang="pl">Nie zapomnij zatwierdzić biletu w sklepie – obowiązkowe, nawet przy krótkim postoju!</p>
      <p class="message message--blue" lang="en">Don't forget to validate your entry ticket in the shop – mandatory, even for short stops!</p>
      <p class="message message--red" lang="ro">Nu uitați să validați biletul în magazin – obligatoriu, chiar și pentru opriri scurte!</p>
      <p class="message message--blue" lang="fr">N'oubliez pas de valider votre ticket à la boutique – obligatoire, même pour un court arrêt !</p>
      <p class="message message--red" lang="de">Vergessen Sie nicht, Ihr Einfahrticket im Shop zu entwerten – Pflicht, auch bei kurzem Parken!</p>
    </div>

    <div class="hours">
      <div class="hours__block hours__block--week">MON – FRI: 05:30 – 22:00</div>
      <div class="hours__block hours__block--weekend">SAT &amp; SUN: 08:00 – 22:00</div>
      <div class="hours__gap"></div>
      <div class="hours__label">Shop Opening Hours</div>
    </div>
  </section>
</div>
</body>
</html>
```